Design a DL Size invitation for End of Year Celebration

Looking for a design to be created for end of year invitation to go to staff and key stakeholders. Invite is to an afternoon sailing Sydney Harbour on a catamaran. The design should demonstrate quality, a bit of fun and is to be printed on white ("lumavel prism" paper stock - you can google this if you need to see it).

I will attach below a copy of our logo in AI / pdf format (please note that attached logo has a cream background - this should be removed before placing in any new artwork)

Dimensions for the artwork should be DL size (210 x 99) with a 3mm bleed in CYMK

Front side - invitation with a place for full name to be added. If artwork is supplied in AI or editable PDF we will update with the individual names.
Reverse side - mainly for details of the event and where to RSVP. This size will not need to be customised for each invitee

```html
<!DOCTYPE html>
<html lang="en">
<head>
<meta charset="utf-8">
<title>Celebrate &amp; Collaborate 2013 – Invitation</title>
<link href="https://fonts.googleapis.com/css2?family=Great+Vibes&family=Luckiest+Guy&family=Fredoka:wght@600&family=Roboto+Condensed:wght@400;700&family=Oswald:wght@300&display=swap" rel="stylesheet">
<style>
  :root {
    --paper: #ffffff;
    --burgundy: #8c2254;
    --burgundy-deep: #78183f;
    --band: #6a1238;
    --gold: #f7bd1a;
    --gold-deep: #eea20a;
    --gold-soft: #d8b25a;
    --ink-light: #f4e3ea;
    --rule: #c98aa6;
    --crop: #9a9a9a;
  }
  * { margin: 0; padding: 0; box-sizing: border-box; }
  html, body { width: 1200px; height: 1200px; overflow: hidden; background: var(--paper); }
  .sheet { position: relative; width: 1200px; height: 1200px; }
  .crop-marks { position: absolute; inset: 0; }

  .panel {
    position: absolute; top: 13px; width: 575px; height: 1170px;
    background: var(--burgundy-deep); overflow: hidden;
  }
  .panel--front { left: 16px; }
  .panel--back { left: 609px; }

  .damask-border { position: absolute; top: 0; bottom: 0; background: var(--burgundy-deep); }
  .damask-border--left { left: 0; width: 68px; }
  .damask-border--right { right: 0; width: 64px; }
  .centre-column { position: absolute; top: 0; bottom: 0; left: 68px; right: 64px; background: var(--burgundy); }

  .title-band { position: absolute; left: 0; width: 544px; top: 71px; height: 93px; background: var(--band); }
  .crest-ornament { position: absolute; left: 258px; width: 60px; border-radius: 4px;
    background: linear-gradient(var(--gold-soft), #a9843a); opacity: .8; }
  .crest-ornament--top { top: 44px; height: 26px; }
  .crest-ornament--bottom { top: 164px; height: 22px; width: 44px; left: 266px; }
  .invitation-word {
    position: absolute; left: 0; width: 576px; top: 82px; text-align: center;
    font-family: "Great Vibes", cursive; font-size: 64px; line-height: 1;
    color: var(--gold-soft);
  }

  .balloons { position: absolute; border-radius: 50% 50% 45% 45%;
    background: radial-gradient(circle at 40% 35%, #f6d23c, #e94b3c 45%, #c93c8e 75%, #3a9be0); }
  .panel--front .balloons { left: 411px; top: 47px; width: 66px; height: 74px; }
  .panel--back .balloons { left: 412px; top: 74px; width: 66px; height: 74px; }

  .brand { position: absolute; left: 164px; top: 216px; width: 248px; height: 47px;
    display: flex; align-items: center; justify-content: center; gap: 10px;
    font-family: "Roboto Condensed", sans-serif; font-weight: 400; font-size: 24px; color: var(--paper); }
  .brand-square { width: 12px; height: 12px; background: var(--paper); }

  .event-title { position: absolute; left: 0; width: 576px; text-align: center; }
  .event-title .celebrate {
    display: block; font-family: "Luckiest Guy", cursive; font-size: 82px; line-height: 1;
    letter-spacing: 1px; color: var(--gold);
    background: linear-gradient(var(--gold), var(--gold-deep)); -webkit-background-clip: text; background-clip: text;
    -webkit-text-fill-color: transparent;
  }
  .event-title .collaborate {
    display: block; margin-top: -10px; padding-left: 40px;
    font-family: "Fredoka", sans-serif; font-weight: 600; font-size: 62px; line-height: 1; color: var(--gold);
  }
  .event-title .amp {
    font-family: "Great Vibes", cursive; font-size: 50px; color: var(--gold-soft); margin-right: 6px;
  }
  .panel--front .event-title { top: 296px; }
  .panel--back .event-title { top: 165px; }

  .year-rule { position: absolute; left: 84px; width: 425px; display: flex; align-items: center; gap: 14px; }
  .year-rule::before, .year-rule::after { content: ""; flex: 1; height: 1px; background: var(--rule); }
  .year-rule span { font-family: "Oswald", sans-serif; font-weight: 300; font-size: 26px; color: var(--gold); line-height: 1; }
  .panel--front .year-rule { top: 428px; }
  .panel--back .year-rule { top: 288px; left: 80px; width: 410px; }

  .detail-list { position: absolute; left: 87px; top: 487px; list-style: none;
    font-family: "Roboto Condensed", sans-serif; font-size: 19px; color: var(--ink-light); }
  .detail-list li { display: flex; height: 34.7px; align-items: center; }
  .detail-list .label { width: 124px; }

  .event-details { position: absolute; left: 0; width: 575px; top: 342px; text-align: center;
    font-family: "Roboto Condensed", sans-serif; font-size: 19px; line-height: 26px; color: var(--ink-light); }
  .event-details h3 { font-weight: 700; font-size: 19px; line-height: 26px; color: var(--paper); margin-top: 8px; }
  .event-details h3:first-child { margin-top: 0; }
  .event-details .gap { margin-top: 8px; }

  .location-map { position: absolute; left: 131px; top: 850px; width: 311px; height: 244px;
    background: linear-gradient(135deg, #a8c9e8, #d9dde0 55%, #b9d3ec); }
</style>
</head>
<body>
<div class="sheet">
  <svg class="crop-marks" width="1200" height="1200" viewBox="0 0 1200 1200" aria-hidden="true">
    <g stroke="var(--crop)" stroke-width="1">
      <line x1="37" y1="1186" x2="37" y2="1200"/><line x1="570" y1="1186" x2="570" y2="1200"/>
      <line x1="630" y1="1186" x2="630" y2="1200"/><line x1="1163" y1="1186" x2="1163" y2="1200"/>
      <line x1="37" y1="0" x2="37" y2="10"/><line x1="570" y1="0" x2="570" y2="10"/>
      <line x1="630" y1="0" x2="630" y2="10"/><line x1="1163" y1="0" x2="1163" y2="10"/>
    </g>
  </svg>

  <section class="panel panel--front">
    <div class="damask-border damask-border--left" role="img" aria-label="Tone-on-tone damask floral pattern"></div>
    <div class="centre-column"></div>
    <div class="damask-border damask-border--right" role="img" aria-label="Tone-on-tone damask floral pattern"></div>

    <div class="title-band"></div>
    <div class="crest-ornament crest-ornament--top" role="img" aria-label="Gold filigree crown ornament"></div>
    <div class="crest-ornament crest-ornament--bottom" role="img" aria-label="Gold filigree scroll ornament"></div>
    <h1 class="invitation-word">Invitation</h1>
    <div class="balloons" role="img" aria-label="Bunch of colourful party balloons"></div>

    <div class="brand"><span class="brand-square"></span>Harbourline Partners</div>

    <h2 class="event-title">
      <span class="celebrate">CELEBRATE</span>
      <span class="collaborate"><span class="amp">&amp;</span>Collaborate</span>
    </h2>
    <div class="year-rule"><span>2013</span></div>

    <ul class="detail-list">
      <li><span class="label">Dummy text</span><span>: Thursday 19th December 2013</span></li>
      <li><span class="label">Dummy text</span><span>: Thursday 19th December 2013</span></li>
      <li><span class="label">Dummy text</span><span>: Thursday 19th December 2013</span></li>
      <li><span class="label">Dummy text</span><span>: Thursday 19th December 2013</span></li>
      <li><span class="label">Dummy text</span><span>: Thursday 19th December 2013</span></li>
      <li><span class="label">Dummy text</span><span>: Thursday 19th December 2013</span></li>
      <li><span class="label">Dummy text</span><span>: Thursday 19th December 2013</span></li>
      <li><span class="label">Dummy text</span><span>: Thursday 19th December 2013</span></li>
      <li><span class="label">Dummy text</span><span>: Thursday 19th December 2013</span></li>
      <li><span class="label">Dummy text</span><span>: Thursday 19th December 2013</span></li>
    </ul>
  </section>

  <section class="panel panel--back">
    <div class="damask-border damask-border--left" role="img" aria-label="Tone-on-tone damask floral pattern"></div>
    <div class="centre-column"></div>
    <div class="damask-border damask-border--right" role="img" aria-label="Tone-on-tone damask floral pattern"></div>

    <div class="balloons" role="img" aria-label="Bunch of colourful party balloons"></div>
    <h2 class="event-title">
      <span class="celebrate">CELEBRATE</span>
      <span class="collaborate"><span class="amp">&amp;</span>Collaborate</span>
    </h2>
    <div class="year-rule"><span>2013</span></div>

    <div class="event-details">
      <h3>DATE:</h3>
      <p>Thursday 19th December 2013</p>
      <h3>TIME:</h3>
      <p>12.00pm Meet at Wattle Cove Wharf</p>
      <p>(Located off Tarrant Rd, next to Harbour Grand Hotel)</p>
      <p class="gap">12.30pm Depart</p>
      <p class="gap">4.30pm Returns to Wattle Cove Wharf</p>
      <h3>EVENT:</h3>
      <p>An afternoon aboard the 48’ sailing catamaran</p>
      <p>Imagine touring the spectacular Sydney Harbour</p>
      <p>including with a gourmet BBQ and drinks.</p>
      <h3>DRESS:</h3>
      <p>Casual summer boat attire</p>
      <p>(stiletto heels cannot be worn).</p>
      <h3>RSVP:</h3>
      <p>mara.ellison@harbourlinepartners.com.au</p>
      <p>02 9000 4172</p>
    </div>

    <div class="location-map" role="img" aria-label="Street map of the harbour showing the wharf meeting point"></div>
  </section>
</div>
</body>
</html>
```